stationary deign for trucking company

im a trucking company looking for a professional set of stationary designs i deliver goods from point a to b
Updates

When submitting stationary designs I need envelope design, letterhead, cards, I’d badge etc

Industry/Entity Type

Trucking Company

Requirements
Must have
• must have letter head, business card, envelope, fax sheet, id badge, folder, thank you card, notebook, invoice sheet.
Nice to have
• nice to have them all custom made (letterhead,envelope, business card, I’d badge etc
Should not have
• must not have prepaid sign want i unique design for items

```html
<!DOCTYPE html>
<html lang="en">
<head>
<meta charset="utf-8">
<title>Harlow Freight Lines — Letterhead &amp; Envelope</title>
<link rel="stylesheet" href="https://fonts.googleapis.com/css2?family=Arimo:wght@400;700&display=swap">
<style>
  :root {
    --canvas: #ffffff;
    --paper: #ffffff;
    --paper-edge: #e2e4e8;
    --band-grey: #d4d4d4;
    --brand-blue: #2a5caa;
    --ink: #1b1b1b;
  }
  * { box-sizing: border-box; margin: 0; padding: 0; }
  html, body { width: 1200px; height: 1200px; overflow: hidden; background: var(--canvas); }
  body { position: relative; font-family: "Arimo", Arial, sans-serif; color: var(--ink); }

  .sheet { position: absolute; background: var(--paper); border: 1px solid var(--paper-edge); }
  .letterhead { left: 63px; top: 68px; width: 823px; height: 1063px; }
  .envelope { left: 404px; top: 530px; width: 753px; height: 376px; }

  .brand-band { position: absolute; background: var(--band-grey); display: flex; align-items: center; }
  .letterhead .brand-band { left: 55px; top: 0; width: 403px; height: 144px; padding-left: 28px; gap: 18px; }
  .envelope .brand-band { left: 46px; top: 3px; width: 165px; height: 225px; align-items: flex-end; padding: 0 0 42px 10px; gap: 8px; }

  .brand-square { flex: none; background: var(--ink); }
  .letterhead .brand-square { width: 44px; height: 44px; }
  .envelope .brand-square { width: 20px; height: 20px; margin-bottom: 3px; }

  .brand-name { font-weight: 700; color: var(--ink); text-transform: uppercase; line-height: 1.05; }
  .letterhead .brand-name { font-size: 34px; letter-spacing: 3px; }
  .envelope .brand-name { font-size: 13px; letter-spacing: 1.2px; }

  .rule { position: absolute; height: 2px; background: var(--brand-blue); }
  .letterhead .rule { left: 0; top: 161px; width: 458px; }
  .envelope .rule { left: 42px; top: 352px; width: 660px; height: 1.5px; }

  .pointer { position: absolute; left: 53px; top: 162px; width: 44px; height: 22px; }

  .contact { position: absolute; list-style: none; }
  .contact li { display: flex; align-items: flex-start; }
  .contact .icon { flex: none; fill: var(--brand-blue); }
  .contact .icon .glyph { fill: none; stroke: #fff; stroke-width: 1.6; stroke-linecap: round; stroke-linejoin: round; }

  .letterhead .contact { left: 69px; top: 201px; font-size: 13.5px; line-height: 16px; }
  .letterhead .contact li { gap: 22px; margin-bottom: 3px; }
  .letterhead .contact li.address { margin-bottom: 10px; }
  .letterhead .contact .icon { width: 15px; height: 15px; }

  .envelope .contact { left: 53px; top: 249px; font-size: 10.5px; line-height: 13px; }
  .envelope .contact li { gap: 12px; margin-bottom: 2.5px; }
  .envelope .contact li.address { margin-bottom: 6px; }
  .envelope .contact .icon { width: 12px; height: 12px; }
</style>
</head>
<body>

<section class="sheet letterhead" aria-label="Letterhead">
  <header class="brand-band">
    <span class="brand-square"></span>
    <span class="brand-name">Harlow<br>Freight Lines</span>
  </header>
  <div class="rule"></div>
  <svg class="pointer" viewBox="0 0 44 22" aria-hidden="true"><polygon points="0,0 44,0 22,22" fill="#2a5caa"/></svg>

  <ul class="contact">
    <li class="address">
      <svg class="icon" viewBox="0 0 16 16"><rect width="16" height="16" rx="3"/><circle class="glyph" cx="8" cy="8" r="4.5"/><path class="glyph" d="M3.5 8h9M8 3.5c2 2.5 2 6.5 0 9M8 3.5c-2 2.5-2 6.5 0 9"/></svg>
      <span>YOUR ADDRESS HERE<br>12345</span>
    </li>
    <li>
      <svg class="icon" viewBox="0 0 16 16"><rect width="16" height="16" rx="3"/><path class="glyph" d="M8 13.2s-3.6-3.6-3.6-6.2a3.6 3.6 0 0 1 7.2 0c0 2.6-3.6 6.2-3.6 6.2z"/><circle class="glyph" cx="8" cy="7" r="1.2"/></svg>
      <span>000111222</span>
    </li>
    <li>
      <svg class="icon" viewBox="0 0 16 16"><rect width="16" height="16" rx="3"/><rect class="glyph" x="5" y="3" width="6" height="10" rx="1"/></svg>
      <span>info@harlowfreight.com</span>
    </li>
    <li>
      <svg class="icon" viewBox="0 0 16 16"><rect width="16" height="16" rx="3"/><rect class="glyph" x="3" y="4.5" width="10" height="7" rx="0.8"/><path class="glyph" d="M3.3 5l4.7 3.6L12.7 5"/></svg>
      <span>harlowfreight.com</span>
    </li>
  </ul>
</section>

<section class="sheet envelope" aria-label="Envelope">
  <header class="brand-band">
    <span class="brand-square"></span>
    <span class="brand-name">Harlow<br>Freight Lines</span>
  </header>

  <ul class="contact">
    <li class="address">
      <svg class="icon" viewBox="0 0 16 16"><rect width="16" height="16" rx="3"/><circle class="glyph" cx="8" cy="8" r="4.5"/><path class="glyph" d="M3.5 8h9M8 3.5c2 2.5 2 6.5 0 9M8 3.5c-2 2.5-2 6.5 0 9"/></svg>
      <span>YOUR ADDRESS HERE<br>12345</span>
    </li>
    <li>
      <svg class="icon" viewBox="0 0 16 16"><rect width="16" height="16" rx="3"/><path class="glyph" d="M8 13.2s-3.6-3.6-3.6-6.2a3.6 3.6 0 0 1 7.2 0c0 2.6-3.6 6.2-3.6 6.2z"/><circle class="glyph" cx="8" cy="7" r="1.2"/></svg>
      <span>000111222</span>
    </li>
    <li>
      <svg class="icon" viewBox="0 0 16 16"><rect width="16" height="16" rx="3"/><rect class="glyph" x="5" y="3" width="6" height="10" rx="1"/></svg>
      <span>info@harlowfreight.com</span>
    </li>
    <li>
      <svg class="icon" viewBox="0 0 16 16"><rect width="16" height="16" rx="3"/><rect class="glyph" x="3" y="4.5" width="10" height="7" rx="0.8"/><path class="glyph" d="M3.3 5l4.7 3.6L12.7 5"/></svg>
      <span>harlowfreight.com</span>
    </li>
  </ul>
  <div class="rule"></div>
</section>

</body>
</html>
```